Brookfarrow Osteopathy and dry needling business card

Business card for Brookfarrow Osteopathy and Dry Needling.

Industry/Entity Type

Health

Contact Information for Business Card

I do not have a phone number yet. I also do not have an email address yet. The physical address is: 48 Lower Crane Street Brookfarrow The website is: www.brookfarrowosteosteopathy.example My details are: Dr Martin Pellowe, Osteopath (B.Clin.Sci (Ost) M.Ost BSC ECON (Hons)

Colors
0094D4
00A9DD
6FCCEA
C7EBF8
E9F6FB

Requirements
Must have
• logo on the back
Nice to have
• Maybe a space for me to write an appointment time and date on the card.

```html
<!DOCTYPE html>
<html lang="en">
<head>
<meta charset="utf-8">
<title>Brookfarrow Osteopathy and Dry Needling – Business Card</title>
<link href="https://fonts.googleapis.com/css2?family=Montserrat:wght@400;500;700;800&display=swap" rel="stylesheet">
<style>
  :root {
    --stage-bg: #404040;
    --brand-blue: #0094D4;
    --brand-blue-mid: #00A9DD;
    --brand-blue-soft: #6FCCEA;
    --brand-accent: #F7941D;
    --card-white: #FFFFFF;
    --ink: #2B2B2B;
    --ink-soft: #4A4A4A;
  }
  * { box-sizing: border-box; margin: 0; padding: 0; }
  html, body { width: 1200px; height: 1000px; overflow: hidden; }
  body {
    background: var(--stage-bg);
    font-family: "Montserrat", sans-serif;
    position: relative;
  }
  .card {
    position: absolute;
    width: 650px;
    height: 374px;
    border-radius: 26px;
    background: var(--card-white);
    overflow: hidden;
    box-shadow: 0 14px 30px rgba(0,0,0,0.35);
  }

  /* Front: appointment card */
  .card--front { left: 276px; top: 103px; }
  .front__banner {
    position: absolute; left: 0; top: 0;
    width: 100%; height: 263px;
    background: radial-gradient(circle at 50% 50%, var(--brand-blue-mid) 0%, var(--brand-blue) 60%);
  }
  .brand-seal {
    position: absolute;
    border-radius: 50%;
    display: flex; align-items: center; justify-content: center;
    text-align: center;
    font-weight: 700;
    text-transform: uppercase;
    letter-spacing: 1.5px;
    line-height: 1.35;
  }
  .brand-seal--front {
    left: 225px; top: 36px;
    width: 200px; height: 200px;
    border: 3px solid var(--card-white);
    color: var(--card-white);
    font-size: 15px;
    padding: 0 24px;
  }
  .appointment-pill {
    position: absolute;
    left: 164px; top: 244px;
    width: 328px; height: 38px;
    background: var(--card-white);
    border: 1.5px solid var(--brand-blue);
    border-radius: 19px;
    display: flex; align-items: center; justify-content: center;
    color: var(--brand-blue);
    font-weight: 800;
    font-size: 18px;
    letter-spacing: 1.2px;
  }
  .appointment-field {
    position: absolute; top: 322px;
    font-size: 18px; color: var(--ink-soft);
    font-weight: 400;
  }
  .appointment-line {
    position: absolute; top: 339px;
    height: 1px; background: var(--ink);
  }
  .appointment-field--date { left: 47px; }
  .appointment-line--date { left: 101px; width: 217px; }
  .appointment-field--time { left: 328px; }
  .appointment-line--time { left: 384px; width: 158px; }
  .appointment-field--ampm { left: 550px; font-size: 15px; top: 325px; }

  /* Back: contact card */
  .card--back { left: 279px; top: 522px; }
  .back__marker {
    position: absolute; left: 0; top: 46px;
    width: 12px; height: 49px;
    background: var(--brand-blue);
  }
  .back__name {
    position: absolute; left: 29px; top: 40px;
    font-size: 26px; font-weight: 800;
    color: var(--brand-blue);
  }
  .back__role {
    position: absolute; left: 29px; top: 78px;
    font-size: 16.5px; font-weight: 400;
    color: var(--ink);
  }
  .contact-list { position: absolute; left: 29px; top: 0; list-style: none; }
  .contact-item {
    position: absolute; left: 0;
    display: flex; align-items: center;
    white-space: nowrap;
    font-size: 17px; color: var(--ink);
  }
  .contact-item svg { width: 17px; height: 17px; margin-right: 9px; flex: none; }
  .contact-item--address { top: 197px; }
  .contact-item--phone { top: 243px; }
  .contact-item--email { top: 271px; }
  .contact-item--web { top: 297px; }
  .brand-seal--back {
    left: 436px; top: 143px;
    width: 188px; height: 188px;
    border: 2px solid var(--brand-blue);
    color: var(--brand-blue);
    font-size: 14px;
    padding: 0 22px;
  }
  .back__accent-line {
    position: absolute; left: 0; top: 349px;
    width: 100%; height: 3px;
    background: var(--brand-accent);
  }
  .back__band {
    position: absolute; left: 0; top: 352px;
    width: 100%; height: 22px;
    background: var(--brand-blue);
  }
</style>
</head>
<body>

<section class="card card--front" aria-label="Appointment card">
  <div class="front__banner"></div>
  <div class="brand-seal brand-seal--front">Brookfarrow Osteopathy and Dry Needling</div>
  <div class="appointment-pill">YOUR NEXT APPOINTMENT</div>
  <span class="appointment-field appointment-field--date">Date :</span>
  <span class="appointment-line appointment-line--date"></span>
  <span class="appointment-field appointment-field--time">Time :</span>
  <span class="appointment-line appointment-line--time"></span>
  <span class="appointment-field appointment-field--ampm">AM/PM</span>
</section>

<section class="card card--back" aria-label="Contact card">
  <div class="back__marker"></div>
  <h1 class="back__name">Dr Martin Pellowe</h1>
  <p class="back__role">Osteopath (B.Clin.Sci (Ost) M.Ost BSC ECON (Hons)</p>

  <ul class="contact-list">
    <li class="contact-item contact-item--address">
      <svg viewBox="0 0 24 24"><path fill="#F7941D" d="M12 1C7.6 1 4 4.5 4 8.9 4 14.8 12 23 12 23s8-8.2 8-14.1C20 4.5 16.4 1 12 1zm0 11a3.2 3.2 0 1 1 0-6.4 3.2 3.2 0 0 1 0 6.4z"/></svg>
      48 Lower Crane Street Brookfarrow
    </li>
    <li class="contact-item contact-item--phone">
      <svg viewBox="0 0 24 24"><path fill="#F7941D" d="M2 9c0-3 4.5-5 10-5s10 2 10 5v2h-5V8.5c-1.5-.6-3.2-.9-5-.9s-3.5.3-5 .9V11H2V9zm4 3h12l2 8H4l2-8z"/></svg>
      +000 555.01.23
    </li>
    <li class="contact-item contact-item--email">
      <svg viewBox="0 0 24 24"><rect x="2" y="5" width="20" height="14" fill="#F7941D"/><path d="M2 5l10 8 10-8M2 19l7-7M22 19l-7-7" stroke="#fff" stroke-width="1.6" fill="none"/></svg>
      info@brookfarrowosteosteopathy.example
    </li>
    <li class="contact-item contact-item--web">
      <svg viewBox="0 0 24 24"><circle cx="12" cy="12" r="10" fill="#F7941D"/><path d="M2 12h20M12 2c3 3 3 17 0 20M12 2c-3 3-3 17 0 20" stroke="#fff" stroke-width="1.4" fill="none"/></svg>
      www.brookfarrowosteosteopathy.example
    </li>
  </ul>

  <div class="brand-seal brand-seal--back">Brookfarrow Osteopathy and Dry Needling</div>
  <div class="back__accent-line"></div>
  <div class="back__band"></div>
</section>

</body>
</html>
```